Online bookstore best-selling book series

I require a website for our book brand. It needs to be appealing (pretty, sweet, feels good to look at it. Functionally it will list five books (a bio for each) available for sale with (square) or (shopify). Also, a few greeting cards and an author bio.

It will also list wholesale prices for bulk.
Please use colors form the books covers, NO ORANGE, YELLOW only pastels that match the covers.

Target Market(s)

women 29 - 55

Coding

Coded - Design and coding required

Number of Pages Required

3 page

Font styles to use
Serif
Script

Requirements
Must have
• a button to shop and add shipping, clean look simply and sweet. very Matching.
Nice to have
• feel good vibe. Happy to be alive feeling.
Should not have
• No orange, yellow, not busy,

```html
<!DOCTYPE html>
<html lang="en">
<head>
<meta charset="utf-8">
<title>The Lucky Ones — Maren Lowe Books</title>
<link href="https://fonts.googleapis.com/css2?family=Gilda+Display&family=Inter:wght@400;500;600;700&display=swap" rel="stylesheet">
<style>
:root{
  --ink:#1a1a1a;
  --text:#444;
  --muted:#7a7a7a;
  --line:#e8e8e8;
  --accent:#ec1e79;
  --star:#f0a830;
  --stock:#2fae4e;
  --side:#f7f7f7;
  --peach:#fde2d4;
  --blush:#fdf1ea;
  --serif:"Gilda Display", Georgia, serif;
  --sans:"Inter", Arial, sans-serif;
}
*{box-sizing:border-box;margin:0;padding:0}
html,body{width:1200px;height:3327px;overflow:hidden;background:#fff}
body{font-family:var(--sans);color:var(--text)}
.page{position:relative;width:1200px;height:3327px;overflow:hidden}
.abs{position:absolute;white-space:nowrap}
.serif{font-family:var(--serif);color:var(--ink);font-weight:400}
.price{color:var(--accent);font-size:18px}
.old{color:var(--muted);text-decoration:line-through;font-size:12px;margin-left:6px}
.fill{position:absolute;border-radius:4px}
.hr{position:absolute;height:1px;background:var(--line)}
svg{display:block}

.topbar{position:absolute;left:0;top:0;width:1200px;height:36px;border-bottom:1px solid var(--line);border-top:2px solid #222;font-size:12px;color:#555}
.topbar span{position:absolute;top:11px}
.logo{font-family:var(--serif);font-size:24px;color:var(--ink);letter-spacing:-0.5px}
.nav a{position:absolute;top:65px;font-size:12px;font-weight:500;letter-spacing:.8px;color:#333;text-decoration:none}
.nav .active::after{content:"";position:absolute;left:8px;top:22px;width:18px;height:2px;background:#333}
.search{position:absolute;left:814px;top:57px;width:196px;height:30px;border-bottom:1px solid #ddd;font-size:12px;color:#777;padding-top:8px}
.circle{position:absolute;width:40px;height:40px;border:1px solid #ddd;border-radius:50%}
.badge{position:absolute;width:16px;height:16px;border-radius:50%;background:var(--accent);color:#fff;font-size:9px;font-weight:700;text-align:center;line-height:16px}
.headband{position:absolute;left:0;top:106px;width:1200px;height:26px;background:linear-gradient(#f6f6f6,#fff)}

.sidebar{position:absolute;left:74px;top:161px;width:206px;height:1379px;background:var(--side)}
.side-search{position:absolute;left:96px;top:182px;width:162px;height:36px;border:1px solid #ddd;background:#fff;font-size:12px;color:#888;padding:11px 14px}
.side-title{font-size:16px;color:var(--ink)}
.side-cat{font-size:12px;color:var(--muted)}
.tag{position:absolute;background:#e5322e;color:#fff;font-size:10px;padding:3px 6px}

.qty{position:absolute;left:748px;width:128px;height:42px;border:1px solid #ddd;font-size:13px;color:#999}
.qty i{position:absolute;top:8px;font-style:normal;font-size:20px;color:#333}
.btn-cart{position:absolute;left:748px;top:803px;width:285px;height:41px;background:#000;color:#fff;font-size:12px;font-weight:600;letter-spacing:.8px;text-align:center;line-height:41px}
.sq{position:absolute;top:803px;width:43px;height:41px;border:1px solid #ddd}
.meta{font-size:13px;color:#444}
.tabs span{position:absolute;top:1072px;font-family:var(--serif);font-size:21px;color:#888}
.desc{font-size:13px;line-height:28px;color:#444;white-space:normal;width:810px}

.card-cat{font-size:12px;color:var(--muted)}
.card-title{font-size:16px;color:var(--ink)}
.stars{font-size:12px;color:var(--star);letter-spacing:2px}
.stars em{font-style:normal;color:var(--muted);letter-spacing:0}

.blush{position:absolute;left:0;top:2713px;width:1200px;height:614px;background:linear-gradient(#fdf3ee,#fdf6f2)}
.infoband{position:absolute;left:74px;top:2648px;width:1065px;height:145px;background:var(--peach)}
.info h3{position:absolute;top:2690px;width:260px;margin-left:-130px;text-align:center;font-family:var(--serif);font-weight:400;font-size:30px;color:var(--ink)}
.info p{position:absolute;top:2737px;width:260px;margin-left:-130px;text-align:center;font-size:12px;color:#777;letter-spacing:.6px}

.foot-h{font-family:var(--serif);font-size:22px;color:var(--ink)}
.foot-l{font-size:13px;color:#555}
.soc{position:absolute;top:3156px;width:11px;height:11px;background:#222;border-radius:2px}
.pay{font-size:14px;font-weight:700;color:#1d2a6b}
</style>
</head>
<body>
<div class="page">

  <div class="topbar">
    <span style="left:74px">▭&nbsp; Welcome Maren Lowe store.</span>
    <span style="left:274px">☏&nbsp; +10 555-014-982</span>
    <span style="left:923px">English ⌄</span>
    <span style="left:1003px">⌂</span>
    <span style="left:1051px">◯&nbsp; My account</span>
  </div>

  <div class="abs logo" style="left:72px;top:56px">MAREN LOWE</div>
  <nav class="nav">
    <a style="left:263px">HOME</a>
    <a style="left:336px">CATEGORIES</a>
    <a class="active" style="left:450px">SHOP</a>
    <a style="left:519px">PAGES</a>
    <a style="left:594px">BLOG</a>
    <a style="left:664px">CONTACT</a>
  </nav>
  <div class="search">Search for items...</div>
  <svg class="abs" style="left:994px;top:64px" width="14" height="14" viewBox="0 0 14 14"><circle cx="6" cy="6" r="4.5" fill="none" stroke="#444" stroke-width="1.4"/><path d="M9.5 9.5L13 13" stroke="#444" stroke-width="1.4"/></svg>
  <div class="circle" style="left:1036px;top:51px"></div>
  <svg class="abs" style="left:1049px;top:64px" width="14" height="14" viewBox="0 0 14 14"><path d="M7 12.5L1.8 7.2A3 3 0 0 1 7 3a3 3 0 0 1 5.2 4.2z" fill="none" stroke="#333" stroke-width="1.2"/></svg>
  <div class="badge" style="left:1060px;top:51px">8</div>
  <div class="circle" style="left:1100px;top:51px"></div>
  <svg class="abs" style="left:1113px;top:63px" width="14" height="16" viewBox="0 0 14 16"><rect x="1.5" y="5" width="11" height="10" fill="none" stroke="#333" stroke-width="1.2"/><path d="M4.5 5V3.5a2.5 2.5 0 0 1 5 0V5" fill="none" stroke="#333" stroke-width="1.2"/></svg>
  <div class="badge" style="left:1124px;top:51px">0</div>
  <div class="headband"></div>

  <div class="abs" style="left:74px;top:126px;font-size:12px;color:#666">Home &nbsp;›&nbsp; Products &nbsp;›&nbsp; <span style="color:#222">The Lucky Ones</span></div>

  <aside class="sidebar"></aside>
  <div class="side-search">Search...</div>
  <svg class="abs" style="left:234px;top:194px" width="13" height="13" viewBox="0 0 14 14"><circle cx="6" cy="6" r="4.5" fill="none" stroke="#444" stroke-width="1.4"/><path d="M9.5 9.5L13 13" stroke="#444" stroke-width="1.4"/></svg>
  <div class="abs serif" style="left:96px;top:254px;font-size:29px">Hot Items</div>

  <div class="fill" role="img" aria-label="Book cover with illustrated comic panels of people reading news" style="left:96px;top:315px;width:162px;height:257px;background:linear-gradient(#fbefdf,#f5e3cc)"></div>
  <div class="tag" style="left:104px;top:326px">- 17%</div>
  <div class="abs side-title" style="left:96px;top:586px">Harriet Vance</div>
  <div class="abs side-title" style="left:96px;top:614px">Portable</div>
  <div class="abs side-cat" style="left:96px;top:650px">Business of Art</div>
  <div class="abs" style="left:96px;top:684px"><span class="price">$10.00</span><span class="old">$12.00</span></div>

  <div class="fill" role="img" aria-label="Book cover with line-art profile and soft peach shapes" style="left:96px;top:749px;width:162px;height:256px;background:linear-gradient(#fbeee6 60%,#f8d9c2)"></div>
  <div class="tag" style="left:104px;top:760px">- 20%</div>
  <div class="abs side-title" style="left:96px;top:1020px">I Am Here Now</div>
  <div class="abs side-cat" style="left:96px;top:1055px">Art &amp; Photography</div>
  <div class="abs price" style="left:96px;top:1088px">$10.00–$20.00</div>

  <div class="fill" role="img" aria-label="Book cover with woman beside a potted tree and blue lettering" style="left:96px;top:1151px;width:162px;height:260px;background:linear-gradient(#fbece3,#f4dccd)"></div>
  <div class="abs side-title" style="left:96px;top:1424px">The Lucky Ones</div>
  <div class="abs side-cat" style="left:96px;top:1459px">Drawing</div>
  <div class="abs price" style="left:96px;top:1492px">$18.00–$45.00</div>

  <div class="fill" role="img" aria-label="Main book cover: woman seated on steps beside a potted tree, blue title lettering" style="left:329px;top:161px;width:375px;height:373px;background:linear-gradient(135deg,#f8e6d8,#f3d9c6)"></div>
  <svg class="abs" style="left:665px;top:182px" width="13" height="13" viewBox="0 0 14 14"><circle cx="6" cy="6" r="4.5" fill="none" stroke="#ec1e79" stroke-width="1.4"/><path d="M9.5 9.5L13 13" stroke="#ec1e79" stroke-width="1.4"/></svg>
  <div class="fill" role="img" aria-label="Thumbnail of front cover" style="left:329px;top:548px;width:63px;height:63px;background:#f5e0cf;outline:1px solid #e6c9b5"></div>
  <div class="fill" role="img" aria-label="Thumbnail of portrait cover" style="left:407px;top:548px;width:63px;height:63px;background:linear-gradient(#e6e4e2,#9c5f5a)"></div>
  <div class="fill" role="img" aria-label="Thumbnail of paper still life cover" style="left:486px;top:548px;width:63px;height:63px;background:#e4ddd3"></div>
  <div class="fill" role="img" aria-label="Thumbnail of hands holding a book" style="left:565px;top:548px;width:63px;height:63px;background:#e2d7cf"></div>

  <h1 class="abs serif" style="left:748px;top:160px;font-size:37px">The Lucky Ones</h1>
  <div class="abs" style="left:748px;top:217px;font-size:12px;color:#777">Author: <span style="color:#222">Maren Lowe</span> &nbsp;<span style="color:#ddd">|</span>&nbsp; <span class="stars">★★★★☆</span> <span style="letter-spacing:.5px">3 Reviews</span></div>
  <div class="hr" style="left:748px;top:254px;width:391px"></div>
  <div class="abs" style="left:748px;top:274px;font-size:25px;color:var(--accent)">$18.00–$45.00</div>
  <div class="abs meta" style="left:748px;top:318px;color:#777">Sold by: &nbsp;<span style="color:#222">Lumen Books</span></div>
  <div class="abs" style="left:748px;top:355px;font-size:12px;color:var(--stock)">✔ In Stock</div>
  <div class="abs" style="left:748px;top:396px;font-size:13px;line-height:23px;color:#777;letter-spacing:.5px">“The Quiet Harbour seems eerily prescient in 2021 . . . Its<br>message is galvanizing and hopeful: We are a nation of<br>scrappy survivors. ”<br>—The Daily Ledger</div>
  <div class="hr" style="left:748px;top:506px;width:391px"></div>

  <div class="abs meta" style="left:748px;top:532px">The Lucky Ones</div>
  <div class="qty" style="top:555px"><i style="left:16px">−</i><span class="abs" style="left:59px;top:13px">0</span><i style="left:98px">+</i></div>
  <div class="abs" style="left:1092px;top:568px;font-size:14px;color:var(--accent)">$45.00</div>
  <div class="abs meta" style="left:748px;top:622px">The Lucky Ones</div>
  <div class="qty" style="top:645px"><i style="left:16px">−</i><span class="abs" style="left:59px;top:13px">0</span><i style="left:98px">+</i></div>
  <div class="abs" style="left:1094px;top:658px;font-size:14px;color:var(--accent)">$18.00</div>
  <div class="abs meta" style="left:748px;top:712px">The Lucky Ones</div>
  <div class="qty" style="top:735px"><i style="left:16px">−</i><span class="abs" style="left:59px;top:13px">0</span><i style="left:98px">+</i></div>
  <div class="abs" style="left:1048px;top:748px;font-size:14px;color:var(--accent)"><span style="color:#999;text-decoration:line-through;font-size:13px">$20.00</span> $18.00</div>

  <div class="btn-cart">Add to cart &nbsp;⧉</div>
  <div class="sq" style="left:1040px"><svg style="margin:13px 0 0 15px" width="14" height="14" viewBox="0 0 14 14"><path d="M7 12.5L1.8 7.2A3 3 0 0 1 7 3a3 3 0 0 1 5.2 4.2z" fill="none" stroke="#333" stroke-width="1.2"/></svg></div>
  <div class="sq" style="left:1090px"><svg style="margin:13px 0 0 15px" width="14" height="14" viewBox="0 0 14 14"><path d="M1 13h12M3 11V6M6 11V3M9 11V7M12 11V5" stroke="#333" stroke-width="1.2"/></svg></div>
  <div class="hr" style="left:748px;top:887px;width:391px"></div>

  <div class="abs meta" style="left:748px;top:908px">SKU: SF1133569600-2</div>
  <div class="abs meta" style="left:748px;top:940px">Category: Drawing</div>
  <div class="abs meta" style="left:748px;top:972px">Tags: book, design, photography</div>
  <div class="abs meta" style="left:748px;top:1003px;color:#777">Share:</div>
  <div class="soc" style="left:802px;top:1006px;background:#666"></div>
  <div class="soc" style="left:828px;top:1006px;background:#666"></div>
  <div class="soc" style="left:854px;top:1006px;background:#666"></div>
  <div class="soc" style="left:880px;top:1006px;background:#666"></div>
  <div class="soc" style="left:906px;top:1006px;background:#666"></div>

  <div class="tabs">
    <span style="left:329px;color:#222">Description</span>
    <span style="left:477px">Product details</span>
    <span style="left:654px">Reviews (3)</span>
    <span style="left:795px">Author</span>
  </div>
  <div class="hr" style="left:329px;top:1117px;width:810px"></div>
  <div class="abs" style="left:329px;top:1116px;width:14px;height:2px;background:#222"></div>

  <div class="abs" style="left:329px;top:1147px;font-size:15px;font-weight:500;color:#222">On the off chance that you have an escalated stop</div>
  <p class="abs desc" style="left:329px;top:1185px">Deep. Understanding. Tenderness. And full of very quiet moments of Maelle.</p>
  <p class="abs desc" style="left:329px;top:1242px">That is what you can see in “Parallel coordinates” – a special re-edition of “5 time zones, 10 hours of flight time and a self-contained eyelash”.</p>
  <p class="abs desc" style="left:329px;top:1327px">With a completely new look with a “strange” idea from the editorial Petal Press, The parallel coordinates will send you a reminder of a strong bond, through space and time in between. past and present, between Paris and Hanoi – two “resident coordinates” associated with the author Maelle.</p>
  <div class="fill" role="img" aria-label="Mockup of a mint paperback beside an open book with spread pages" style="left:329px;top:1441px;width:810px;height:286px;border-radius:0;background:linear-gradient(90deg,#c8b2aa,#d9c7c0 55%,#bfa69e)"></div>
  <p class="abs desc" style="left:329px;top:1756px">“One can do so many things with the iron and blue chair in the Tuileries Garden. Sit up and read, watch the sky, watch the people, watch the ducks swim in the fountains, the long lines in front of the Gelato Rosa ice cream vans, in front of the Musée de l'Orangerie and the Jeu de Center Paume, or shoots a couple whispering on another nearby chair.</p>

  <h2 class="abs serif" style="left:74px;top:1928px;font-size:29px">Related products</h2>
  <div class="hr" style="left:74px;top:1978px;width:1065px"></div>

  <div class="fill" role="img" aria-label="Book cover: folded paper on a cream wall, serif title" style="left:74px;top:2016px;width:246px;height:388px;background:linear-gradient(#eee9e1,#ded6cb)"></div>
  <div class="abs stars" style="left:74px;top:2423px">★★★★★ <em>(1 Review)</em></div>
  <div class="abs card-title" style="left:74px;top:2449px">The Lucky Ones</div>
  <div class="abs card-cat" style="left:74px;top:2477px">Biography &amp; Memoirs</div>
  <div class="abs" style="left:74px;top:2506px"><span class="price">$18.00</span><span class="old">$20.00</span></div>

  <div class="fill" role="img" aria-label="Book cover: pink background with a blue dish and lollipop" style="left:347px;top:2016px;width:246px;height:388px;background:linear-gradient(#fcc0c0,#f7a8aa)"></div>
  <div class="abs stars" style="left:347px;top:2423px">★★★★★ <em>(1 Review)</em></div>
  <div class="abs card-title" style="left:347px;top:2449px">The Lucky Ones</div>
  <div class="abs card-cat" style="left:347px;top:2477px">Graphic Design</div>
  <div class="abs" style="left:347px;top:2506px"><span class="price">$18.00</span><span class="old">$20.00</span></div>

  <div class="fill" role="img" aria-label="Book cover: illustrated songbirds on a blush background" style="left:620px;top:2016px;width:247px;height:388px;background:linear-gradient(#faede5,#f4ddd0)"></div>
  <div class="abs stars" style="left:620px;top:2423px">★★★★★ <em>(1 Review)</em></div>
  <div class="abs card-title" style="left:620px;top:2449px">The Lucky Ones</div>
  <div class="abs card-cat" style="left:620px;top:2477px">Romance</div>
  <div class="abs" style="left:620px;top:2506px"><span class="price">$35.00</span><span class="old">$45.00</span></div>

  <div class="fill" role="img" aria-label="Book cover: portrait photograph with soft smoke, large serif title" style="left:894px;top:2016px;width:245px;height:388px;background:linear-gradient(#e8e7e6,#a9706d)"></div>
  <div class="abs stars" style="left:894px;top:2423px">★★★★★ <em>(1 Review)</em></div>
  <div class="abs card-title" style="left:894px;top:2449px">The Lucky Ones</div>
  <div class="abs card-cat" style="left:894px;top:2477px">One Business</div>
  <div class="abs price" style="left:894px;top:2506px">$20.00</div>

  <div class="blush"></div>
  <div class="infoband"></div>
  <div class="info">
    <h3 style="left:207px">Store location</h3><p style="left:207px">14 Willow Court Apt. 22</p>
    <h3 style="left:473px">Contact Us</h3><p style="left:473px">hello@pagebloom.com</p>
    <h3 style="left:739px">Call Us</h3><p style="left:739px">+10 555 014 902</p>
    <h3 style="left:1005px">Opening Hours</h3><p style="left:1005px">Mon – Sat : 00.00 – 10.00</p>
  </div>

  <div class="abs logo" style="left:66px;top:2914px;font-size:36px">MAREN LOWE</div>
  <div class="abs foot-l" style="left:66px;top:3002px;line-height:28px">⚲&nbsp; 48 Linden Row Apt. 12,<br>&nbsp;&nbsp;&nbsp;&nbsp;&nbsp;Harbourton 20410, USA</div>
  <div class="abs foot-l" style="left:66px;top:3066px">✉&nbsp; info@marenlowe.com</div>
  <div class="abs foot-l" style="left:66px;top:3109px;color:var(--accent)">☏&nbsp; (+10) 555014509</div>
  <div class="soc" style="left:66px"></div>
  <div class="soc" style="left:99px"></div>
  <div class="soc" style="left:132px"></div>
  <div class="soc" style="left:168px"></div>
  <div class="soc" style="left:203px"></div>

  <div class="abs foot-h" style="left:430px;top:2922px">Customer Service</div>
  <div class="abs foot-l" style="left:430px;top:2981px">Shipping Options</div>
  <div class="abs foot-l" style="left:430px;top:3020px">My Wishlist</div>
  <div class="abs foot-l" style="left:430px;top:3057px">My Account</div>
  <div class="abs foot-l" style="left:430px;top:3096px">Return Policy</div>
  <div class="abs foot-l" style="left:430px;top:3135px">Shopping FAQs</div>

  <div class="abs foot-h" style="left:673px;top:2922px">Our Store</div>
  <div class="abs foot-l" style="left:673px;top:2981px">About us</div>
  <div class="abs foot-l" style="left:673px;top:3020px">Terms of Service</div>
  <div class="abs foot-l" style="left:673px;top:3057px">Privacy Policy</div>
  <div class="abs foot-l" style="left:673px;top:3096px">Our Blogs</div>
  <div class="abs foot-l" style="left:673px;top:3135px">Contact Us</div>

  <div class="abs foot-h" style="left:984px;top:2922px">Our Newsletter</div>
  <div class="abs" style="left:920px;top:2976px;width:212px;text-align:right;white-space:normal;font-size:12px;line-height:16px;color:#666;letter-spacing:.4px">Leave your email to get all hot deals &amp; news which benefit you most!</div>
  <div class="abs" style="left:916px;top:3051px;font-size:12px;color:#777">Your email address</div>
  <div class="abs" style="left:1085px;top:3051px;font-size:12px;font-weight:600;color:var(--accent);letter-spacing:.6px">Submit</div>
  <div class="hr" style="left:916px;top:3078px;width:216px;background:#ddd"></div>

  <div class="hr" style="left:66px;top:3236px;width:1073px;background:#eadfd9"></div>
  <div class="abs" style="left:66px;top:3272px;font-size:12px;color:#666;letter-spacing:.6px">© 2023 Maren Lowe. All Rights Reserved. Design and Developed by fernline studio.</div>
  <div class="abs pay" style="left:913px;top:3270px">Cardline &nbsp; Orbit &nbsp; Swiftpay &nbsp; Paynest</div>

  <div class="abs" style="left:1160px;top:3278px;width:40px;height:40px;border-radius:50%;background:var(--accent)"></div>
  <svg class="abs" style="left:1171px;top:3288px" width="18" height="18" viewBox="0 0 18 18"><path d="M3 9l6-6 6 6M3 15l6-6 6 6" fill="none" stroke="#fff" stroke-width="2"/></svg>

</div>
</body>
</html>
```